Bref créative
Brivona Real Estate
Professional
Tom Radcliffe
President
782 W. Hollow Pine Rd. Suite 310
Beverly Hills, CA 90210
tom@BrivonaRealEstate.example
www.BrivonaRealEstate.example
I will upload our logo. If there is a problem with that please use logo on web site www.brivonarealestate.example
Please use our logo.

```html
<!DOCTYPE html>
<html lang="en">
<head>
<meta charset="utf-8">
<title>Brivona Real Estate – Business Card</title>
<link href="https://fonts.googleapis.com/css2?family=Arimo:wght@400;700&display=swap" rel="stylesheet">
<style>
  :root {
    --page-bg: #e9e6e1;
    --card-blue: #a9c3e4;
    --card-mid: #dbe6f3;
    --card-white: #ffffff;
    --ink-dark: #1b1f2a;
    --ink-body: #3d4350;
    --brand-navy: #1f3f7a;
    --tagline-blue: #3d6fb8;
    --tile-blue: #c9d9ee;
  }
  * { margin: 0; padding: 0; box-sizing: border-box; }
  html, body {
    width: 1200px;
    height: 906px;
    overflow: hidden;
    background: var(--page-bg);
    font-family: "Arimo", Arial, sans-serif;
  }
  .business-card {
    position: absolute;
    left: 75px;
    top: 153px;
    width: 1050px;
    height: 600px;
    background: linear-gradient(100deg, var(--card-blue) 0%, var(--card-mid) 35%, var(--card-white) 62%, var(--card-mid) 88%, var(--card-blue) 100%);
    overflow: hidden;
    box-shadow: 0 8px 24px rgba(0,0,0,0.18);
  }
  .decor-field {
    position: absolute;
    left: 0;
    top: 0;
    width: 520px;
    height: 440px;
    background: radial-gradient(ellipse at 45% 25%, var(--tile-blue) 0%, rgba(201,217,238,0.45) 45%, rgba(201,217,238,0) 70%);
  }
  .holder {
    position: absolute;
    right: 44px;
    top: 32px;
    text-align: right;
  }
  .holder-name {
    font-size: 40px;
    font-weight: 700;
    color: var(--ink-dark);
    line-height: 1.1;
  }
  .holder-title {
    font-size: 28px;
    color: var(--ink-dark);
    line-height: 1.3;
  }
  .brand {
    position: absolute;
    left: 360px;
    top: 236px;
    width: 640px;
    display: flex;
    align-items: center;
    gap: 20px;
  }
  .brand-mark {
    flex: 0 0 auto;
    width: 68px;
    height: 68px;
    background: var(--brand-navy);
  }
  .brand-name {
    font-size: 38px;
    font-weight: 700;
    letter-spacing: 2px;
    color: var(--brand-navy);
    white-space: nowrap;
  }
  .tagline {
    position: absolute;
    left: 376px;
    top: 336px;
    font-size: 22px;
    font-weight: 700;
    letter-spacing: 2.5px;
    color: var(--tagline-blue);
    white-space: nowrap;
  }
  .contact {
    position: absolute;
    top: 496px;
    font-size: 23px;
    line-height: 1.38;
    color: var(--ink-body);
    white-space: nowrap;
  }
  .contact-address { left: 44px; }
  .contact-online { left: 370px; }
  .contact-phones { right: 44px; text-align: right; }
</style>
</head>
<body>
  <div class="business-card">
    <div class="decor-field" role="img" aria-label="Soft blue field of translucent rounded tiles"></div>

    <div class="holder">
      <div class="holder-name">Tom Radcliffe</div>
      <div class="holder-title">President</div>
    </div>

    <div class="brand">
      <div class="brand-mark"></div>
      <div class="brand-name">BRIVONA REAL ESTATE</div>
    </div>
    <div class="tagline">Investments • Brokerage • Solutions</div>

    <div class="contact contact-address">
      782 W. Hollow Pine Rd.<br>
      Suite 310 Beverly Hills,<br>
      CA 90210
    </div>
    <div class="contact contact-online">
      tom@BrivonaRealEstate.example<br>
      www.BrivonaRealEstate.example
    </div>
    <div class="contact contact-phones">
      Ph: 310-555-0142<br>
      Cell: 310-555-0187<br>
      Fax: 866-555-0163
    </div>
  </div>
</body>
</html>
```